Bref créative
Modern Architecture Diagram for Data Warehouse Testing Software
The DataFlint Architecture
Our product, DataFlint, is Web 2.0 software that enables data warehouse QA teams to automate bulk comparison of their data and to validate 100% of data throughout the ETL process. We would like to feature a diagram of the architecture of the tool for people visiting our website and to feature on print materials. We have our old diagram attached, and would like some different ideas. These diagrams are just different versions of the diagrams we’ve used in the past, so that the designers could understand the architecture better.
Information Technology
Corporate, technical, modern
Please keep the graphic as simple as possible, we are open to new ideas and prefer that the icons are clean and simple, and have a similar look. There are no particular dimensions. The diagram has to be clearly viewed on a website and on printed sales materials (8.5’’ x 11’’ sheet of paper) .
Most recent Architecture diagram
Another diagram we were using, this one uses desktops for the agents
Beginning of an idea we had to change how the diagram looked. (Doesn't have the necessary arrows)
an example of the one of the types of look and feel that we like (from the Velorant website)

```html
<!DOCTYPE html>
<html lang="en">
<head>
<meta charset="utf-8">
<title>Architecture Diagram</title>
<link href="https://fonts.googleapis.com/css2?family=Open+Sans:wght@400&display=swap" rel="stylesheet">
<style>
  :root {
    --canvas: #ffffff;
    --panel: #29a8e0;
    --ink: #ffffff;
    --pane: #e9ecef;
    --pane-shade: #cfd6dc;
  }
  html, body { margin: 0; padding: 0; overflow: hidden; background: var(--canvas); }
  .architecture {
    width: 1200px; height: 871px; display: block;
    font-family: "Open Sans", Arial, sans-serif;
  }
  .panel-field { fill: var(--panel); }
  .divider { fill: none; stroke: var(--canvas); stroke-width: 8; stroke-linejoin: miter; }
  .label { fill: var(--ink); font-size: 31px; text-anchor: middle; }
  .icon-fill { fill: var(--ink); }
  .icon-line { fill: none; stroke: var(--ink); }
  .icon-cut { fill: var(--panel); }
</style>
</head>
<body>
<svg class="architecture" viewBox="0 0 1200 871" xmlns="http://www.w3.org/2000/svg" role="img" aria-label="System architecture: users, browser-based UI, database, app server and agents">
  <rect class="panel-field" x="100" y="92" width="1020" height="676"/>

  <path class="divider" d="M440 92 V225 L460 250 L440 275 V430"/>
  <path class="divider" d="M100 430 H580 L600 410 L620 430 H1120"/>
  <path class="divider" d="M432 430 V578 L452 600 L432 622 V768"/>
  <path class="divider" d="M782 430 V578 L762 600 L782 622 V768"/>

  <g class="icon user-icon">
    <ellipse class="icon-fill" cx="272" cy="190" rx="40" ry="45"/>
    <path class="icon-fill" d="M212 252 Q272 232 332 252 Q342 258 342 272 V318 H202 V272 Q202 258 212 252 Z"/>
    <path class="icon-cut" d="M258 244 L272 262 L286 244 Z"/>
  </g>
  <text class="label" x="265" y="388">Users</text>

  <g class="icon browser-icon">
    <rect class="icon-line" x="664" y="145" width="222" height="178" rx="14" stroke-width="8"/>
    <line class="icon-line" x1="690" y1="173" x2="850" y2="173" stroke-width="5"/>
    <circle class="icon-fill" cx="862" cy="160" r="3"/>
    <circle class="icon-fill" cx="872" cy="160" r="3"/>
    <rect x="688" y="186" width="174" height="116" fill="var(--pane)"/>
    <polygon points="688,186 862,302 688,302" fill="var(--ink)"/>
    <rect x="850" y="186" width="12" height="116" fill="var(--pane-shade)"/>
  </g>
  <text class="label" x="780" y="388">Browser-based UI</text>

  <g class="icon database-icon">
    <path class="icon-fill" d="M200 520 Q266 490 332 520 V548 Q266 578 200 548 Z"/>
    <path class="icon-fill" d="M200 558 Q266 588 332 558 V586 Q266 616 200 586 Z"/>
    <path class="icon-fill" d="M200 596 Q266 626 332 596 V624 Q266 654 200 624 Z"/>
    <path class="icon-fill" d="M200 634 Q266 664 332 634 V646 Q266 676 200 646 Z"/>
  </g>
  <text class="label" x="265" y="732">Database</text>

  <g class="icon server-icon">
    <rect class="icon-fill" x="560" y="492" width="92" height="180" rx="6"/>
    <circle class="icon-cut" cx="606" cy="528" r="10"/>
    <rect class="icon-cut" x="578" y="630" width="56" height="4"/>
    <rect class="icon-cut" x="578" y="640" width="56" height="4"/>
    <rect class="icon-cut" x="578" y="650" width="56" height="4"/>
  </g>
  <text class="label" x="607" y="732">App Server</text>

  <g class="icon gears-icon">
    <g transform="translate(908 604)">
      <circle class="icon-fill" r="46"/>
      <g class="icon-fill">
        <rect x="-11" y="-62" width="22" height="124"/>
        <rect x="-11" y="-62" width="22" height="124" transform="rotate(45)"/>
        <rect x="-11" y="-62" width="22" height="124" transform="rotate(90)"/>
        <rect x="-11" y="-62" width="22" height="124" transform="rotate(135)"/>
      </g>
      <circle class="icon-cut" r="22"/>
    </g>
    <g transform="translate(1000 568)">
      <circle class="icon-fill" r="32"/>
      <g class="icon-fill">
        <rect x="-8" y="-44" width="16" height="88"/>
        <rect x="-8" y="-44" width="16" height="88" transform="rotate(45)"/>
        <rect x="-8" y="-44" width="16" height="88" transform="rotate(90)"/>
        <rect x="-8" y="-44" width="16" height="88" transform="rotate(135)"/>
      </g>
      <circle class="icon-cut" r="15"/>
    </g>
    <g transform="translate(946 522)">
      <circle class="icon-fill" r="22"/>
      <g class="icon-fill">
        <rect x="-6" y="-30" width="12" height="60"/>
        <rect x="-6" y="-30" width="12" height="60" transform="rotate(45)"/>
        <rect x="-6" y="-30" width="12" height="60" transform="rotate(90)"/>
        <rect x="-6" y="-30" width="12" height="60" transform="rotate(135)"/>
      </g>
      <circle class="icon-cut" r="10"/>
    </g>
  </g>
  <text class="label" x="950" y="732">Agents</text>
</svg>
</body>
</html>
```